Podcast cover art for Steady Harbor Podcast for Busy Parents

I am relaunching my 3 year podcast under a new name. The podcast is called Steady Harbor for Busy Parents. The parent company is called Bright Path Studio (see attached logo) and should be represented on the cover in a small way. Previously the show was called Bright Path Studio. We talk about creating life balance for working moms by focusing on faith, marriage, parenting, career, health, home, finances, and friends/fun. I don't mind having stock photography on the cover but I prefer not to have my image on it as it is not a personal brand. I have attached a couple of stock images as inspiration.

Target Market(s)

working Christian moms age 30-45 income 75,000+, working full time, Christian faith, married

Industry/Entity Type

Media

Font styles to use
Serif

Requirements
Must have
• Podcast name: Steady Harbor for Busy Parents
• By: Bright Path Studio (include logo)
• I also included my brand sheet for reference which includes my brand colors and fonts. Navy should be the primary with orange and gray as the accents
Should not have
• No flowers, or overly girly. My brand is more clean, preppy, and young-sophisticated.

```html
<!DOCTYPE html>
<html lang="en">
<head>
<meta charset="utf-8">
<title>Steady Harbor for Busy Parents — Podcast Cover</title>
<link href="https://fonts.googleapis.com/css2?family=Josefin+Sans:wght@300;400&display=swap" rel="stylesheet">
<style>
  :root {
    --navy: #272a35;
    --ink: #111214;
    --orange: #e87a3c;
    --gray: #aba7a5;
    --white: #ffffff;
    --paper: #ffffff;
    --title-font: "Josefin Sans", sans-serif;
  }
  * { margin: 0; padding: 0; box-sizing: border-box; }
  html, body {
    width: 1200px;
    height: 1200px;
    overflow: hidden;
    background: var(--paper);
  }
  .cover {
    position: relative;
    width: 1200px;
    height: 1200px;
    background: var(--paper);
    font-family: var(--title-font);
  }
  .cover-ring {
    position: absolute;
    left: 58px;
    top: 58px;
    width: 1084px;
    height: 1084px;
    border-radius: 50%;
    border: 16px solid var(--orange);
    overflow: hidden;
  }
  .cover-photo {
    position: absolute;
    inset: 0;
    background:
      radial-gradient(circle at 88% 30%, rgba(176, 96, 52, 0.75) 0%, rgba(176, 96, 52, 0) 28%),
      radial-gradient(circle at 20% 22%, rgba(150, 128, 112, 0.55) 0%, rgba(150, 128, 112, 0) 35%),
      radial-gradient(circle at 18% 70%, rgba(196, 150, 128, 0.55) 0%, rgba(196, 150, 128, 0) 26%),
      radial-gradient(circle at 70% 95%, rgba(255, 255, 255, 0.95) 0%, rgba(255, 255, 255, 0) 45%),
      linear-gradient(170deg, #d9d6d3 0%, #c8c6c6 35%, #b9bcc3 60%, #e6e8ec 100%);
  }
  .axis-line {
    position: absolute;
    left: 599px;
    top: 78px;
    width: 2px;
    height: 818px;
    background: var(--ink);
  }
  .title-block {
    position: absolute;
    height: 125px;
    display: flex;
    align-items: center;
    justify-content: center;
    white-space: nowrap;
    line-height: 1;
  }
  .title-block span { display: block; padding-top: 12px; }
  .title-block--steady {
    left: 374px; top: 184px; width: 452px;
    background: var(--navy);
    color: var(--white);
    font-weight: 400;
    font-size: 80px;
    letter-spacing: 2px;
  }
  .title-block--harbor {
    left: 267px; top: 308px; width: 512px;
    background: var(--ink);
    color: var(--orange);
    font-weight: 300;
    font-size: 104px;
  }
  .title-block--for {
    left: 502px; top: 433px; width: 164px;
    background: var(--gray);
    color: var(--navy);
    font-weight: 400;
    font-size: 72px;
  }
  .title-block--busy {
    left: 464px; top: 558px; width: 546px;
    background: var(--navy);
    color: var(--white);
    font-weight: 300;
    font-size: 104px;
  }
  .title-block--parents {
    left: 300px; top: 682px; width: 560px;
    background: var(--navy);
    color: var(--orange);
    font-weight: 300;
    font-size: 104px;
  }
  .studio-name {
    position: absolute;
    left: 0;
    width: 1200px;
    top: 1030px;
    text-align: center;
    font-family: var(--title-font);
    font-weight: 400;
    font-size: 46px;
    color: var(--ink);
  }
</style>
</head>
<body>
  <main class="cover">
    <div class="cover-ring">
      <div class="cover-photo" role="img" aria-label="Soft-focus stock photo of a woman writing in a spiral planner with a blue pen at a desk"></div>
    </div>
    <div class="axis-line"></div>
    <h1 class="podcast-title">
      <div class="title-block title-block--steady"><span>Steady</span></div>
      <div class="title-block title-block--harbor"><span>HARBOR</span></div>
      <div class="title-block title-block--for"><span>for</span></div>
      <div class="title-block title-block--busy"><span>BUSY</span></div>
      <div class="title-block title-block--parents"><span>PARENTS</span></div>
    </h1>
    <p class="studio-name">Bright Path Studio</p>
  </main>
</body>
</html>
```